Brine - Pop/Rock Album Artwork

Brine are a London based Rock/Indie band and this is our 2nd album. We require CD cover artwork.
Here is the artwork for our first album: https://www.vendrilo.co.uk/gp/product/X913QK44Z2?ie=UTF8&*Version*=1&*entries*=0
We like the following attached CD Covers and we are in the same genre music as these bands.
The Album will be called "Paper Hollow", the band name "BRINE" should be uppercase. Ideally the name "BRINE" will be designed in such a way that we can use this font on badges and as a Logo itself.
The track listing is:-
1 Unspun
2. 40 Tides
3. Rusty Gale
4. Kestrels
5. Bellows
6. Fold the Amber
7. Herons
8. Palmora
9. Out by Dusk
10. Pale Ember
11. Unfurl
This project should really just cover the front page of the artwork for a digital CD artwork to be used on Cadenzo and Wavvel.
Please do listen to our music here: https://echovault.com/brine

```html
<!DOCTYPE html>
<html lang="en">
<head>
<meta charset="utf-8">
<title>BRINE — Paper Hollow</title>
<link href="https://fonts.googleapis.com/css2?family=Italiana&display=swap" rel="stylesheet">
<style>
  :root {
    --rust: #b04a1c;
    --amber: #c87a1e;
    --mustard: #b8921a;
    --plum: #7a3a4e;
    --rose: #a2474e;
    --ink-light: #ffffff;
  }
  html, body {
    margin: 0;
    padding: 0;
    width: 1200px;
    height: 1200px;
    overflow: hidden;
    background: var(--rust);
  }
  .cover {
    position: relative;
    width: 1200px;
    height: 1200px;
    overflow: hidden;
  }
  .cover__artwork {
    position: absolute;
    inset: 0;
    background:
      radial-gradient(circle at 12% 55%, var(--plum) 0 18%, transparent 32%),
      radial-gradient(circle at 85% 40%, var(--rose) 0 14%, transparent 30%),
      radial-gradient(circle at 78% 30%, var(--mustard) 0 8%, transparent 20%),
      radial-gradient(circle at 40% 10%, var(--amber) 0 16%, transparent 34%),
      radial-gradient(circle at 55% 75%, var(--plum) 0 12%, transparent 30%),
      radial-gradient(circle at 20% 90%, var(--rust) 0 16%, transparent 34%),
      radial-gradient(circle at 90% 90%, var(--amber) 0 10%, transparent 28%),
      linear-gradient(135deg, var(--rust), var(--amber) 45%, var(--rust) 70%, var(--plum));
  }
  .cover__title {
    position: absolute;
    left: 0;
    right: 0;
    top: 0;
    display: flex;
    flex-direction: column;
    align-items: center;
    font-family: "Italiana", serif;
    color: var(--ink-light);
  }
  .band-name {
    margin: 338px 0 0;
    font-size: 330px;
    line-height: 1;
    font-weight: 400;
    letter-spacing: 6px;
  }
  .title-rule {
    width: 756px;
    height: 2px;
    margin-top: 24px;
    background: var(--ink-light);
  }
  .album-name {
    margin: 26px 0 0;
    font-size: 112px;
    line-height: 1;
    font-weight: 400;
    letter-spacing: 2px;
  }
</style>
</head>
<body>
  <main class="cover">
    <div class="cover__artwork" role="img" aria-label="Abstract painted brush-stroke loops in rust orange, amber, mustard, plum and rose with fine white speckles"></div>
    <div class="cover__title">
      <h1 class="band-name">BRINE</h1>
      <div class="title-rule"></div>
      <h2 class="album-name">PAPER HOLLOW</h2>
    </div>
  </main>
</body>
</html>
```